Meridian Rest Supply Needs Business Card

Looking for a very nice looking business card. Creative but not extravagant. We sell beds and pillows across the U.S. and need something professional but catchy. I have attached the logo.

Name : Dale Fenwick
Title : President
Phone : (800) 417-2964
Email: sleep@quorvana.com
Website: www.quorvana.com

Can be single-sided or double-sided
horizontal or vertical

Can use Blues/Greys

Target Market(s)

Mass Market

Industry/Entity Type

Retail

Contact Information for Business Card

Name : Dale Fenwick
Title : President
Phone : (800) 417-2964
Email: sleep@quorvana.com
Website: www.quorvana.com

Requirements
Must have
• Clean, Modern, Smooth
• Can use Blues/Greys
• On the other side without the information - have something simple like www.quorvana.com or our logo
Nice to have
• Surprise me
Should not have
• Nothing crazy, nothing cluttered

```html
<!DOCTYPE html>
<html lang="en">
<head>
<meta charset="utf-8">
<title>Quorvana Business Card</title>
<link rel="stylesheet" href="https://fonts.googleapis.com/css2?family=Open+Sans:wght@400;600&display=swap">
<style>
  :root {
    --page-bg: #ecebe9;
    --card-grey: #6d6e71;
    --card-grey-light: #7a7b7e;
    --band-white: #f7f7f7;
    --name-ink: #5b5c60;
    --text-light: #ffffff;
    --text-muted: #e4e4e4;
    --icon-bg: #2f3033;
    --shadow: rgba(0, 0, 0, 0.18);
  }
  * { box-sizing: border-box; margin: 0; padding: 0; }
  html, body {
    width: 1200px;
    height: 800px;
    overflow: hidden;
    background: var(--page-bg);
    font-family: "Open Sans", Arial, sans-serif;
  }
  .canvas {
    position: relative;
    width: 1200px;
    height: 800px;
  }
  .card {
    position: absolute;
    left: 320px;
    width: 560px;
    height: 320px;
    overflow: hidden;
    box-shadow: 0 6px 18px var(--shadow);
    background: linear-gradient(180deg, var(--card-grey-light), var(--card-grey));
  }
  .card--back { top: 40px; }
  .card--front { top: 430px; }

  /* Company name placeholder: plain text in the card's own font */
  .company-name {
    font-family: "Open Sans", Arial, sans-serif;
    font-weight: 600;
    color: var(--name-ink);
    line-height: 1;
    white-space: nowrap;
  }

  /* Back side */
  .back-band {
    position: absolute;
    left: 0;
    top: 105px;
    width: 100%;
    height: 110px;
    background: var(--band-white);
    display: flex;
    align-items: center;
    justify-content: center;
  }
  .back-band .company-name { font-size: 34px; }

  /* Front side */
  .front-strip {
    position: absolute;
    left: 0;
    top: 0;
    width: 158px;
    height: 100%;
    background: var(--band-white);
  }
  .front-strip .company-name {
    position: absolute;
    left: 50%;
    top: 50%;
    font-size: 30px;
    transform: translate(-50%, -50%) rotate(-90deg);
  }
  .contact-block {
    position: absolute;
    left: 250px;
    top: 92px;
    color: var(--text-light);
  }
  .person-name {
    font-size: 18px;
    font-weight: 600;
    line-height: 1.15;
    margin-left: 28px;
  }
  .person-title {
    font-size: 14px;
    font-weight: 400;
    color: var(--text-muted);
    margin-left: 28px;
    margin-bottom: 18px;
  }
  .contact-list { list-style: none; }
  .contact-item {
    display: flex;
    align-items: center;
    font-size: 14px;
    height: 25px;
  }
  .contact-icon {
    width: 18px;
    height: 18px;
    background: var(--icon-bg);
    margin-right: 10px;
    display: flex;
    align-items: center;
    justify-content: center;
    flex: none;
  }
  .contact-icon svg { width: 11px; height: 11px; }
</style>
</head>
<body>
<main class="canvas">
  <section class="card card--back" aria-label="Card back">
    <div class="back-band">
      <span class="company-name">quorvana</span>
    </div>
  </section>

  <section class="card card--front" aria-label="Card front">
    <div class="front-strip">
      <span class="company-name">quorvana</span>
    </div>
    <div class="contact-block">
      <p class="person-name">Dale Fenwick</p>
      <p class="person-title">President</p>
      <ul class="contact-list">
        <li class="contact-item">
          <span class="contact-icon">
            <svg viewBox="0 0 12 12" aria-hidden="true"><path d="M3 1 L5 1 L5.5 3.5 L4.3 4.3 Q5 6.8 7.7 7.7 L8.5 6.5 L11 7 L11 9 Q10.5 11 8.5 11 Q1 10 1 3.5 Q1 1 3 1 Z" fill="#ffffff"/></svg>
          </span>
          (800) 417-2964
        </li>
        <li class="contact-item">
          <span class="contact-icon">
            <svg viewBox="0 0 12 12" aria-hidden="true"><rect x="1" y="2.5" width="10" height="7" fill="#ffffff"/><path d="M1 2.5 L6 6.5 L11 2.5" fill="none" stroke="#2f3033" stroke-width="1"/></svg>
          </span>
          sleep@quorvana.com
        </li>
        <li class="contact-item">
          <span class="contact-icon">
            <svg viewBox="0 0 12 12" aria-hidden="true"><g fill="none" stroke="#ffffff" stroke-width="1"><circle cx="6" cy="6" r="4.8"/><ellipse cx="6" cy="6" rx="2" ry="4.8"/><line x1="1.2" y1="6" x2="10.8" y2="6"/></g></svg>
          </span>
          www.quorvana.com
        </li>
      </ul>
    </div>
  </section>
</main>
</body>
</html>
```